Used Car Dealer seeks an Amazing Business Card Design

We are looking for a business card design that incorporates our logo and grabs the attention of anyone we give the business card to.

Looking to use the same colors as the logo. Our Logo choice is the black background with Red and Silver/Grey Lettering.

We also would like to see some embossed designs.

Target Market(s)

Used Car Buyers, Automotive, Auto

Industry/Entity Type

Automotive

Contact Information for Business Card

BVEX7K
Gordon Whitley
482 Tenbrook Lane
Suite 305
Roswell, GA 30098
Office (770) 555-0142
Cell (770) 555-0187
bvex7kga@mailnest.example
www.bvex7kga.example

Colors
ffffff
ee3036

Requirements
Must have
• Must include our logo (Black Background with Red and Silver/Grey Lettering)
Nice to have
• Embossed Design. Can be Single or Double Sided.

```html
<!DOCTYPE html>
<html lang="en">
<head>
<meta charset="utf-8">
<title>BVEX7K Business Card</title>
<link rel="stylesheet" href="https://fonts.googleapis.com/css2?family=Open+Sans:wght@400;600;700&display=swap">
<style>
  :root {
    --page: #ebebeb;
    --card-black: #060606;
    --brand-red: #c20d14;
    --text-red: #d0121b;
    --text-light: #e6e6e6;
  }
  html, body {
    margin: 0;
    width: 1200px;
    height: 900px;
    overflow: hidden;
    background: var(--page);
    font-family: "Open Sans", Arial, sans-serif;
  }
  .canvas { position: relative; width: 1200px; height: 900px; }
  .card {
    position: absolute;
    width: 556px;
    height: 344px;
    background: var(--card-black);
    overflow: hidden;
    box-shadow: 0 6px 18px rgba(0,0,0,0.25);
  }
  .card-front { left: 360px; top: 48px; }
  .card-back { left: 458px; top: 518px; width: 559px; }
  .front-art { position: absolute; inset: 0; }
  .holder-name {
    position: absolute; left: 29px; top: 143px; margin: 0;
    font-size: 26px; font-weight: 600; color: var(--text-red); line-height: 34px;
  }
  .contact-list {
    position: absolute; left: 29px; top: 218px; margin: 0; padding: 0;
    list-style: none; color: var(--text-light); font-size: 17px; line-height: 26px;
  }
  .contact-list li { display: flex; align-items: center; gap: 10px; white-space: nowrap; }
  .contact-icon { width: 12px; height: 12px; fill: var(--text-red); flex: none; }
  .address {
    position: absolute; right: 31px; top: 252px; margin: 0;
    text-align: right; font-style: normal; color: var(--text-light);
    font-size: 16px; line-height: 23px; white-space: nowrap;
  }
  .brand-name {
    position: absolute; left: 0; right: 0; top: 142px; margin: 0;
    text-align: center; font-size: 52px; font-weight: 700;
    color: var(--text-red); letter-spacing: 1px; line-height: 60px;
  }
</style>
</head>
<body>
<main class="canvas">
  <section class="card card-front" aria-label="Business card front">
    <svg class="front-art" width="556" height="344" viewBox="0 0 556 344" role="img" aria-label="Red top band with a curved black panel; a silver arc decoration belongs along the curve">
      <rect width="556" height="344" fill="var(--brand-red)"/>
      <path d="M0,72 Q300,20 556,216 L556,344 L0,344 Z" fill="var(--card-black)"/>
    </svg>
    <h1 class="holder-name">Gordon Whitley</h1>
    <ul class="contact-list">
      <li><svg class="contact-icon" viewBox="0 0 12 12"><path d="M1,3 Q6,0 11,3 L10,5 L8,4 L8,3 Q6,2 4,3 L4,4 L2,5 Z M3,6 L9,6 L10,11 L2,11 Z"/></svg>(770) 555-0142</li>
      <li><svg class="contact-icon" viewBox="0 0 12 12"><path d="M3,0 H9 V12 H3 Z M4,1.5 V9 H8 V1.5 Z" fill-rule="evenodd"/></svg>(770) 555-0187</li>
      <li><svg class="contact-icon" viewBox="0 0 12 12"><path d="M0,2 H12 V10 H0 Z M0.8,2.6 L6,6.5 L11.2,2.6 Z" fill-rule="evenodd"/></svg>bvex7kga@mailnest.example</li>
      <li><svg class="contact-icon" viewBox="0 0 12 12"><circle cx="6" cy="6" r="5.5"/></svg>www.bvex7kga.example</li>
    </ul>
    <address class="address">482 Tenbrook Lane<br>Suite 305<br>Roswell, GA 30098</address>
  </section>

  <section class="card card-back" aria-label="Business card back">
    <p class="brand-name">BVEX7K</p>
  </section>
</main>
</body>
</html>
```